Introduction flyer

Bright Orchard Nutrition & Wellness Consulting, is a new holistic nutritional therapy specialising in womens health. I want a flyer that appeals to women between 15 to 60. It must speak "health, food & balance". I have attached the basic info I need included in the text. I like Greens & Blues, soft text. My flyer will be distributed to cafes, shops, fitness centres, hung up in grocery stores & health centres etc. The QEVR & WRUK logos need to appear on the flyer to show I am fully registered. My own logo & company name is attached.

Target Market(s)

Women from 10 to 60 years old.

Industry/Entity Type

Nutritionist

Colors
32a6d7
abd037
33b8a4
fbf289
ffcf3e
b768aa
d5d5d5
dcdcdc
e8e8e8

Requirements
Must have
• An image of healthy food & ladies. A group of women eating soup, stews or curry type dishes, with plenty of colour - no bread or white wine, and not just fruit please. Food that looks enjoyable to the average person.
• Nutrition is main part of my job, so please keep that in mind & emphasise food & natural well being.
Should not have
• People exercising, men, white wine, bread, cakes, sweets etc..

```html
<!DOCTYPE html>
<html lang="en">
<head>
<meta charset="utf-8">
<title>Bright Orchard Nutrition &amp; Wellness Consulting – Flyer</title>
<link href="https://fonts.googleapis.com/css2?family=Source+Sans+3:wght@400;600;700&display=swap" rel="stylesheet">
<style>
  :root {
    --teal: #5bbcaa;
    --teal-deep: #3fae9b;
    --lime: #abd037;
    --lime-soft: #c3d95a;
    --blue: #32a6d7;
    --logo-blue: #2f6db3;
    --yellow: #ffd65a;
    --grey-disc: #f0f0f0;
    --text-grey: #555555;
    --orange: #f0562e;
    --white: #ffffff;
  }
  * { box-sizing: border-box; margin: 0; padding: 0; }
  html, body { width: 858px; height: 1200px; overflow: hidden; background: #ffffff; }
  body { font-family: "Source Sans 3", Arial, sans-serif; }
  .flyer { position: relative; width: 858px; height: 1200px; overflow: hidden; background: var(--white); }

  .hero-photo {
    position: absolute; left: 0; top: 0; width: 858px; height: 430px;
    background: radial-gradient(ellipse at 55% 45%, #d8b49a 0%, #a98a74 35%, #6f5f55 70%, #4e4844 100%);
  }
  .consult-badge {
    position: absolute; left: 47px; top: 122px; width: 252px; height: 252px; border-radius: 50%;
    background: rgba(171, 208, 55, 0.85);
    display: flex; align-items: center; justify-content: center; text-align: center;
    color: var(--white); font-size: 19px; line-height: 27px; text-transform: uppercase;
  }
  .question-band {
    position: absolute; left: 0; top: 430px; width: 858px; height: 80px;
    background: var(--teal);
    display: flex; align-items: center; justify-content: center; text-align: center;
    color: var(--white); font-weight: 700; font-size: 22px; line-height: 29px; text-transform: uppercase;
  }
  .backdrop { position: absolute; left: 0; top: 525px; }

  .brand { position: absolute; left: 40px; top: 548px; width: 380px; text-align: center; color: var(--logo-blue); }
  .brand-dot { width: 70px; height: 70px; border-radius: 50%; background: var(--logo-blue); margin: 8px auto 28px; opacity: .9; }
  .brand-name { font-weight: 600; font-size: 20px; line-height: 22px; letter-spacing: .3px; }

  .intro { position: absolute; left: 34px; width: 300px; color: var(--white); font-size: 16px; line-height: 24px; white-space: nowrap; }
  .intro-lead { top: 756px; font-weight: 700; text-transform: uppercase; font-size: 15.5px; }
  .intro-eat { top: 854px; }
  .intro-body { top: 974px; }
  .intro-web { position: absolute; left: 34px; top: 1160px; color: var(--white); font-weight: 700; font-size: 15px; }

  .food-photo {
    position: absolute; left: 313px; top: 756px; width: 155px; height: 155px; border-radius: 50%;
    border: 5px solid var(--white);
    background: radial-gradient(circle at 45% 45%, #e7c9a8 0%, #6f9a45 45%, #c65a3c 75%, #f2ece4 100%);
  }
  .specialist { position: absolute; left: 478px; top: 604px; width: 370px; }
  .specialist-title { text-align: center; color: var(--blue); font-weight: 700; font-size: 15px; line-height: 24.5px; margin-bottom: 16px; }
  .specialist-list { list-style: none; }
  .specialist-list li { position: relative; padding-left: 28px; color: var(--text-grey); font-size: 12.5px; line-height: 14px; margin-bottom: 16px; }
  .specialist-list svg { position: absolute; left: 4px; top: 0; }
  .produce-photo {
    position: absolute; left: 668px; top: 784px; width: 172px; height: 146px; border-radius: 12px;
    background: radial-gradient(ellipse at 50% 50%, #e9c46a 0%, #d98a55 45%, #9cbf5a 100%);
    opacity: .9;
  }

  .contact { position: absolute; left: 380px; top: 1037px; width: 440px; text-align: center; }
  .contact-call { color: var(--orange); font-weight: 700; font-size: 15.5px; line-height: 20px; }
  .contact-note { margin-top: 10px; color: var(--blue); font-size: 9px; line-height: 10.5px; }
</style>
</head>
<body>
<main class="flyer">
  <div class="hero-photo" role="img" aria-label="Photo of a smiling woman in a kitchen eating a bowl of vegetable soup"></div>
  <div class="consult-badge">Consultations<br>available<br>at your home,<br>work or at my office</div>
  <div class="question-band">Do you experience low energy, low libido, menstrual<br>cycle complications, or are you planninga baby?</div>

  <svg class="backdrop" width="858" height="675" viewBox="0 0 858 675" aria-hidden="true">
    <circle cx="30" cy="330" r="190" fill="var(--lime-soft)"/>
    <circle cx="450" cy="490" r="110" fill="var(--lime)"/>
    <path d="M0 250 C 120 215 300 220 400 300 C 470 360 470 520 440 675 L0 675 Z" fill="var(--teal)"/>
    <circle cx="652" cy="262" r="236" fill="var(--grey-disc)"/>
    <circle cx="595" cy="695" r="232" fill="var(--yellow)"/>
    <circle cx="400" cy="470" r="50" fill="var(--teal-deep)" opacity=".55"/>
  </svg>

  <div class="brand">
    <div class="brand-dot"></div>
    <div class="brand-name">BRIGHT ORCHARD NUTRITION<br>&amp; Wellness Consulting</div>
  </div>

  <p class="intro intro-lead">Small changes to your diet<br>may lead to big changes in your<br>health.</p>
  <p class="intro intro-eat">Eat well, live well.<br>Discover exactly what YOU need to<br>change and how to make these changes<br>long lasting.</p>
  <p class="intro intro-body">There is no one-rule-fits-all. In consulta-<br>tions, I aim to dig up the root cause to your<br>health concerns. I will support you on your<br>journey to regain health and be the best<br>version of you. My nutrition and lifestyle<br>plans are personalised to your needs and<br>set of circumstances.</p>
  <div class="intro-web">www.brightorchardnutrition.ie</div>

  <div class="food-photo" role="img" aria-label="Round photo of a fresh salad with apple slices and spinach"></div>

  <section class="specialist">
    <h2 class="specialist-title">Qualified, Registered and fully insured<br>Nutritional Therapist &amp; Wellness Consultant,<br>specialising in:</h2>
    <ul class="specialist-list">
      <li><svg width="14" height="14" viewBox="0 0 14 14"><circle cx="7" cy="7" r="6" fill="none" stroke="var(--lime)" stroke-width="1.3"/><path d="M4 7.2l2 2 4-4" fill="none" stroke="var(--lime)" stroke-width="1.4"/></svg>Fertility, IVF, pre-conception, pregnancy &amp; post-natal care</li>
      <li><svg width="14" height="14" viewBox="0 0 14 14"><circle cx="7" cy="7" r="6" fill="none" stroke="var(--lime)" stroke-width="1.3"/><path d="M4 7.2l2 2 4-4" fill="none" stroke="var(--lime)" stroke-width="1.4"/></svg>Menstrual cycle challenges<br>(PCOS, Endometriosis, PMS, heavy/irregular periods etc)</li>
      <li><svg width="14" height="14" viewBox="0 0 14 14"><circle cx="7" cy="7" r="6" fill="none" stroke="var(--lime)" stroke-width="1.3"/><path d="M4 7.2l2 2 4-4" fill="none" stroke="var(--lime)" stroke-width="1.4"/></svg>Thyroid conditions</li>
      <li><svg width="14" height="14" viewBox="0 0 14 14"><circle cx="7" cy="7" r="6" fill="none" stroke="var(--lime)" stroke-width="1.3"/><path d="M4 7.2l2 2 4-4" fill="none" stroke="var(--lime)" stroke-width="1.4"/></svg>Low libido</li>
      <li><svg width="14" height="14" viewBox="0 0 14 14"><circle cx="7" cy="7" r="6" fill="none" stroke="var(--lime)" stroke-width="1.3"/><path d="M4 7.2l2 2 4-4" fill="none" stroke="var(--lime)" stroke-width="1.4"/></svg>Digestive health</li>
      <li><svg width="14" height="14" viewBox="0 0 14 14"><circle cx="7" cy="7" r="6" fill="none" stroke="var(--lime)" stroke-width="1.3"/><path d="M4 7.2l2 2 4-4" fill="none" stroke="var(--lime)" stroke-width="1.4"/></svg>Hormonal imbalances</li>
      <li><svg width="14" height="14" viewBox="0 0 14 14"><circle cx="7" cy="7" r="6" fill="none" stroke="var(--lime)" stroke-width="1.3"/><path d="M4 7.2l2 2 4-4" fill="none" stroke="var(--lime)" stroke-width="1.4"/></svg>Perimenopause/menopause</li>
      <li><svg width="14" height="14" viewBox="0 0 14 14"><circle cx="7" cy="7" r="6" fill="none" stroke="var(--lime)" stroke-width="1.3"/><path d="M4 7.2l2 2 4-4" fill="none" stroke="var(--lime)" stroke-width="1.4"/></svg>Weight management</li>
      <li><svg width="14" height="14" viewBox="0 0 14 14"><circle cx="7" cy="7" r="6" fill="none" stroke="var(--lime)" stroke-width="1.3"/><path d="M4 7.2l2 2 4-4" fill="none" stroke="var(--lime)" stroke-width="1.4"/></svg>Type 2 diabetes, blood sugar dysregulation,<br>high blood pressure, high cholesterol</li>
    </ul>
  </section>

  <div class="produce-photo" role="img" aria-label="Arrangement of colourful fresh fruit and vegetables"></div>

  <section class="contact">
    <p class="contact-call">Call Aisling today on<br>085-4627-391<br>or email aisling@brightorchardnutrition.ie<br>to book a consultation or for a free<br>no obligation 15-minute mini consultation.</p>
    <p class="contact-note">Initial consultations typically last up to 2 hours, follow-ups 30 – 60 minutes.<br>Further investigative tests may be recommended such as blood, urine, salvia<br>sampling. These will always be agreed with the client in advance.</p>
  </section>
</main>
</body>
</html>
```